web design for specialty coffee shop

We are online shop selling specialty coffeee.
Our brand concept keywords are -
specialty coffee, knowledge, discovery, professional, convenience, collaboration.
there will be five main tabs on the homepage
[home (u icon from logo)]
[coffee]
[equipment]
[gift]
[knowledge]
[about us]
For our site, we will be using the following template.
ONLY DESIGN, NO CODING necessary as our developers will do that.
http://layoutbarn.example/item/velorina-deluxe-adaptive-storefront-theme/full_screen_preview/7351620
Use the template as a base.
You do not have to do exactly the same layout.
Creative Liberty!
For the style and color palette, please look at the attached image.
Our brown logo should match nicely with the style provided in the attachment.
Thank you for taking the time to read this post.
Looking forward to working with artmingle and the amazing designers that are part of this community.
Reason: Dear designers,
I have extended the deadline to give designers who accepted to participate in this contest some more time to submit their designs. Thank you for understanding.

```html
<!DOCTYPE html>
<html lang="en">
<head>
<meta charset="utf-8">
<title>Kestrel Coffee Lab</title>
<link rel="stylesheet" href="https://fonts.googleapis.com/css2?family=Patua+One&family=Yanone+Kaffeesatz:wght@300;400&family=Arimo&family=Kalam:wght@700&display=swap">
<style>
:root{
  --wood:#e2a862;
  --wood-light:#f0c488;
  --plank-line:rgba(150,85,30,.45);
  --top-bar:#2b0a08;
  --logo-bg:#3a0c06;
  --logo-frame:#7a2a10;
  --logo-text:#f1c983;
  --link:#eab168;
  --nav-bg:#f9ebd2;
  --nav-text:#9c2b10;
  --hero-border:#e25a26;
  --hero-brown:#9a5421;
  --band-dark:#4b1a0a;
  --band-light:#c98a3e;
  --title:#f0cf9c;
  --sub:#f6c14c;
  --panel-frame:#7a3a1c;
  --panel-frame-light:#a0583a;
  --panel-bg:#2b0303;
  --icon:#8a4a17;
  --icon-dark:#5e2e0e;
  --label:#f4d9b0;
  --ink:#2a0805;
  --dot-active:#e25a26;
}
*{margin:0;padding:0;box-sizing:border-box}
html,body{width:1200px;height:709px;overflow:hidden}
body{
  position:relative;font-family:'Arimo',Arial,sans-serif;
  background:
    repeating-linear-gradient(90deg,transparent 0 23px,var(--plank-line) 23px 24px),
    repeating-linear-gradient(90deg,rgba(255,230,180,.25) 0 6px,transparent 6px 11px,rgba(170,100,40,.12) 11px 17px,transparent 17px 24px),
    repeating-linear-gradient(90deg,transparent 0 48px,rgba(180,110,45,.18) 48px 72px,transparent 72px 120px),
    linear-gradient(90deg,var(--wood) 0%,var(--wood-light) 30%,var(--wood) 55%,var(--wood-light) 80%,var(--wood) 100%);
}
.top-bar{position:absolute;left:0;top:0;width:1200px;height:55px;background:
  repeating-linear-gradient(90deg,rgba(0,0,0,.12) 0 2px,transparent 2px 7px),var(--top-bar)}
.account-links{position:absolute;left:802px;top:13px;font-family:'Patua One',serif;font-size:15px;color:var(--link);white-space:nowrap}
.account-links span{position:absolute;top:0}
.brand{position:absolute;left:216px;top:0;width:234px;height:156px;
  background:repeating-linear-gradient(90deg,rgba(0,0,0,.15) 0 2px,transparent 2px 9px),var(--logo-bg);
  border:0 solid var(--logo-frame);border-width:0 17px 13px;display:flex;flex-direction:column;align-items:center;justify-content:center;gap:10px;
  box-shadow:0 2px 4px rgba(60,20,0,.4)}
.brand-mark{width:22px;height:22px;background:var(--logo-text);border-radius:50%}
.brand-name{font-family:'Patua One',serif;font-size:24px;color:var(--logo-text);text-align:center;line-height:1}
.main-nav{position:absolute;left:493px;top:65px;width:483px;height:37px;background:var(--nav-bg);border-radius:6px;box-shadow:0 2px 3px rgba(80,30,0,.3);font-family:'Patua One',serif;font-size:18px;color:var(--nav-text)}
.main-nav span{position:absolute;top:7px;white-space:nowrap}
.hero{position:absolute;left:236px;top:178px;width:729px;height:232px;border:2px solid var(--hero-border);border-radius:7px;overflow:hidden;background:var(--hero-brown)}
.hero-photo{position:absolute;left:0;top:0;width:520px;height:100%;
  background:radial-gradient(ellipse 60% 45% at 22% 85%,#f2ede6 0%,#e6d8c8 40%,transparent 70%),
  linear-gradient(100deg,#8a4a28 0%,#c98457 25%,#b36c40 55%,var(--hero-brown) 100%)}
.hero-band{position:absolute;left:267px;top:0;right:0;height:86px;background:linear-gradient(90deg,var(--band-light),var(--band-dark));text-align:center}
.hero-title{font-family:'Yanone Kaffeesatz',sans-serif;font-weight:300;font-size:42px;color:var(--title);margin-top:10px;line-height:1}
.hero-sub{font-size:18px;color:var(--sub);margin-top:7px}
.slider-dots{position:absolute;left:641px;top:201px;display:flex;gap:5px}
.slider-dots span{width:11px;height:11px;border-radius:50%;background:#fff}
.slider-dots .active{background:var(--dot-active)}
.how-title{position:absolute;left:545px;top:433px;font-family:'Patua One',serif;font-size:17px;color:var(--ink);white-space:nowrap}
.how-arrow{position:absolute;left:700px;top:436px}
.steps{position:absolute;left:236px;top:466px;width:730px;height:160px;background:var(--panel-bg);
  border:solid var(--panel-frame);border-width:12px 11px 11px;border-radius:6px;
  box-shadow:inset 0 0 0 2px var(--panel-frame-light),0 2px 4px rgba(60,20,0,.4)}
.step{position:absolute;top:11px;width:180px;margin-left:-90px;text-align:center}
.step svg{display:block;margin:0 auto 10px}
.step-label{font-size:10.4px;line-height:13px;color:var(--label)}
.copyright{position:absolute;left:490px;top:690px;font-size:10px;color:#000;white-space:nowrap}
.connect{position:absolute;left:889px;top:652px;font-family:'Kalam',cursive;font-size:11px;color:#000}
.social{position:absolute;left:896px;top:670px;width:30px;height:31px;background:#7a3a1c;border-radius:5px}
</style>
</head>
<body>
<header class="top-bar">
  <nav class="account-links"><span style="left:0">sign in</span><span style="left:62px">register</span><span style="left:131px">cart (0)</span></nav>
</header>
<div class="brand">
  <span class="brand-mark"></span>
  <span class="brand-name">Kestrel<br>Coffee Lab</span>
</div>
<nav class="main-nav">
  <span style="left:28px">Shop</span><span style="left:96px">Subscription</span><span style="left:230px">Gift</span><span style="left:285px">Knowledge</span><span style="left:407px">FAQ</span>
</nav>
<section class="hero">
  <div class="hero-photo" role="img" aria-label="Close-up photo of a woman smelling coffee from a white cup"></div>
  <div class="hero-band">
    <h1 class="hero-title">Choose your taste !</h1>
    <p class="hero-sub">in 3 easy steps</p>
  </div>
  <div class="slider-dots"><span></span><span></span><span></span><span class="active"></span><span></span></div>
</section>
<h2 class="how-title">HOW IT WORKS !</h2>
<svg class="how-arrow" width="30" height="28" viewBox="0 0 30 28"><path d="M3 4 Q22 0 24 18" fill="none" stroke="#2a0805" stroke-width="2.5" stroke-linecap="round"/><path d="M18 14 L24 22 L28 12" fill="none" stroke="#2a0805" stroke-width="2.5" stroke-linecap="round" stroke-linejoin="round"/></svg>
<section class="steps">
  <div class="step" style="left:75px">
    <svg width="90" height="82" viewBox="0 0 90 82" aria-label="Cup with dollar sign">
      <path d="M38 2 q-5 6 0 12 q4 6 0 12 M45 2 q-5 6 0 12 q4 6 0 12" fill="none" stroke="#f4d9b0" stroke-width="2.5" stroke-linecap="round"/>
      <circle cx="30" cy="55" r="14" fill="none" stroke="var(--icon-dark)" stroke-width="6"/>
      <rect x="30" y="26" width="50" height="55" rx="6" fill="var(--icon)"/>
      <text x="55" y="63" text-anchor="middle" font-family="Arimo,Arial,sans-serif" font-size="24" fill="#e0a040">$</text>
    </svg>
    <p class="step-label">CHOOSE YOUR<br>SUBSCRIPTION</p>
  </div>
  <div class="step" style="left:247px">
    <svg width="90" height="82" viewBox="0 0 90 82" aria-label="Open box">
      <polygon points="0,16 38,12 48,32 12,34" fill="var(--icon)"/>
      <polygon points="48,32 58,8 90,14 80,34" fill="var(--icon)"/>
      <polygon points="12,34 48,32 46,82 14,74" fill="var(--icon-dark)"/>
      <polygon points="48,32 80,34 78,72 46,82" fill="var(--icon)"/>
      <polygon points="14,26 48,22 80,26 48,32" fill="#3a1508"/>
    </svg>
    <p class="step-label">YOUR KESTREL<br>BOX DELIVERED</p>
  </div>
  <div class="step" style="left:419px">
    <svg width="90" height="82" viewBox="0 0 90 82" aria-label="Coffee beans">
      <g fill="none" stroke="var(--icon)" stroke-width="4">
        <ellipse cx="54" cy="28" rx="18" ry="25" transform="rotate(-30 54 28)"/>
        <path d="M44 10 q14 16 20 36"/>
        <ellipse cx="20" cy="50" rx="10" ry="20"/>
        <path d="M20 32 q-4 18 0 36"/>
        <ellipse cx="60" cy="70" rx="20" ry="10"/>
        <path d="M42 70 q18 -4 36 0"/>
      </g>
    </svg>
    <p class="step-label">BREW 4 COFFEES<br>AND PICK A FAVOURITE</p>
  </div>
  <div class="step" style="left:605px">
    <svg width="90" height="82" viewBox="0 0 90 82" aria-label="Coffee bag">
      <path d="M32 22 v-8 a13 13 0 0 1 26 0 v8" fill="none" stroke="var(--icon)" stroke-width="5"/>
      <rect x="15" y="20" width="60" height="62" rx="6" fill="var(--icon)"/>
    </svg>
    <p class="step-label">GET A FULL BAG<br>WITH FREE SHIPPING</p>
  </div>
</section>
<span class="connect">Connect</span>
<span class="social" aria-label="Social page"></span>
<footer class="copyright">© copyright Kestrel Coffee Lab 2013. All rights reserved</footer>
</body>
</html>
```